BRSP Business Card Design Project

We are a Wedding Film company in Charleston, SC In need of a unique business card. Our website is www.brightspiralreels.example. Check us out to get an idea of who we are and what we do. The design should be upscale but not pretentious. Modern but not cheesy. I will most likely have our cards printed by Zib on the Opal design. I'm also liking the raised designs for our logo. The Wedding Films in our logo on our site is blue so feel free to manipulate our logo for your designs as well.

Industry/Entity Type

Business

Requirements
Must have
• This is the info I want on the card:

Derek Hollisbury
Storyteller

Brightspiral Wedding Reels
www.brightspiralreels.example

555.208.4417
derek@brightspiralreels.example

```html
<!DOCTYPE html>
<html lang="en">
<head>
<meta charset="utf-8">
<title>Brightspiral Wedding Reels — Business Card</title>
<link rel="stylesheet" href="https://fonts.googleapis.com/css2?family=Open+Sans:wght@400;600;700&display=swap">
<style>
  :root {
    --backdrop: #ece8e1;
    --card: #ffffff;
    --gold-dark: #8f7a4c;
    --gold-mid: #b9a56e;
    --gold-light: #ddd0a0;
    --ink-brown: #8a7348;
    --ink-soft: #9b8a66;
    --white: #ffffff;
  }
  * { box-sizing: border-box; margin: 0; padding: 0; }
  html, body { width: 1200px; height: 665px; overflow: hidden; }
  body {
    background: var(--backdrop);
    font-family: "Open Sans", Arial, sans-serif;
    position: relative;
  }
  .card {
    position: absolute;
    top: 188px;
    width: 504px;
    height: 288px;
    background: var(--card);
    overflow: hidden;
    box-shadow: 0 4px 14px rgba(0,0,0,0.12);
  }
  .card--front { left: 64px; }
  .card--back { left: 632px; }
  .swoosh { position: absolute; inset: 0; width: 100%; height: 100%; }
  .brand {
    position: absolute;
    display: flex;
    flex-direction: column;
    align-items: center;
    color: var(--ink-brown);
    font-weight: 600;
    text-align: center;
  }
  .brand__mark {
    border-radius: 50%;
    background: var(--gold-mid);
  }
  .card--front .brand { left: 30px; top: 38px; width: 190px; gap: 12px; }
  .card--front .brand__mark { width: 70px; height: 70px; }
  .card--front .brand__name { font-size: 19px; line-height: 1.2; }
  .card--back .brand { left: 112px; top: 50px; width: 280px; gap: 14px; }
  .card--back .brand__mark { width: 96px; height: 96px; }
  .card--back .brand__name { font-size: 18px; line-height: 1.2; white-space: nowrap; }
  .person { position: absolute; left: 246px; top: 34px; }
  .person__name { font-size: 16px; font-weight: 700; color: var(--ink-brown); }
  .person__role { font-size: 11px; color: var(--ink-soft); margin-top: 2px; }
  .contact {
    position: absolute; left: 246px; top: 98px;
    list-style: none; font-size: 11px; color: var(--ink-brown);
  }
  .contact li { display: flex; align-items: center; gap: 6px; margin-bottom: 6px; }
  .contact svg { width: 10px; height: 10px; fill: var(--ink-soft); }
  .website {
    position: absolute;
    color: var(--white);
    font-size: 13px;
    font-weight: 700;
  }
  .card--front .website { left: 28px; bottom: 18px; }
  .card--back .website { left: 24px; top: 228px; }
</style>
</head>
<body>
  <section class="card card--front" aria-label="Business card front">
    <svg class="swoosh" viewBox="0 0 504 288" preserveAspectRatio="none" aria-hidden="true">
      <defs>
        <linearGradient id="goldFront" x1="0" y1="0" x2="1" y2="0">
          <stop offset="0" stop-color="var(--gold-dark)"/>
          <stop offset="0.45" stop-color="var(--gold-light)"/>
          <stop offset="1" stop-color="var(--gold-dark)"/>
        </linearGradient>
      </defs>
      <path d="M180 214 C280 182 380 166 504 160 L504 166 C380 172 280 188 180 214 Z" fill="url(#goldFront)"/>
      <path d="M0 240 C140 200 300 176 504 172 L504 288 L0 288 Z" fill="url(#goldFront)"/>
      <path d="M0 250 C140 210 300 186 504 182" fill="none" stroke="var(--white)" stroke-width="2"/>
    </svg>
    <div class="brand">
      <span class="brand__mark" aria-hidden="true"></span>
      <span class="brand__name">Brightspiral Wedding Reels</span>
    </div>
    <div class="person">
      <p class="person__name">Derek Hollisbury</p>
      <p class="person__role">Storyteller</p>
    </div>
    <ul class="contact">
      <li>
        <svg viewBox="0 0 10 10" aria-hidden="true"><path d="M2 0.5 L3.6 0.5 L4.2 2.8 L3 3.6 C3.6 5 4.9 6.3 6.4 7 L7.2 5.8 L9.5 6.4 L9.5 8 C9.5 9 8.8 9.6 7.8 9.5 C3.9 9 1 6.1 0.5 2.2 C0.4 1.2 1 0.5 2 0.5 Z"/></svg>
        555.208.4417
      </li>
      <li>
        <svg viewBox="0 0 10 10" aria-hidden="true"><path d="M0 2 L10 2 L10 8.5 L0 8.5 Z M0.8 2.6 L5 5.6 L9.2 2.6 L9.2 3.4 L5 6.4 L0.8 3.4 Z" fill-rule="evenodd"/></svg>
        derek@brightspiralreels.example
      </li>
    </ul>
    <p class="website">www.brightspiralreels.example</p>
  </section>

  <section class="card card--back" aria-label="Business card back">
    <svg class="swoosh" viewBox="0 0 504 288" preserveAspectRatio="none" aria-hidden="true">
      <defs>
        <linearGradient id="goldBack" x1="0" y1="0" x2="1" y2="0">
          <stop offset="0" stop-color="var(--gold-dark)"/>
          <stop offset="0.5" stop-color="var(--gold-light)"/>
          <stop offset="1" stop-color="var(--gold-dark)"/>
        </linearGradient>
      </defs>
      <path d="M0 204 C160 196 330 240 504 256 L504 288 L0 288 Z" fill="url(#goldBack)"/>
      <path d="M0 196 C170 186 330 232 504 246" fill="none" stroke="var(--white)" stroke-width="3"/>
      <path d="M260 214 C340 232 420 240 504 240 L504 234 C420 232 340 226 260 214 Z" fill="url(#goldBack)"/>
    </svg>
    <div class="brand">
      <span class="brand__mark" aria-hidden="true"></span>
      <span class="brand__name">Brightspiral Wedding Reels</span>
    </div>
    <p class="website">www.brightspiralreels.example</p>
  </section>
</body>
</html>
```